Entrepreneur needs a business card design

I need a business card to name my three companies, as well as contact information.
I'm open on design and color and it can be plain or complex. I'm open on colors but I think I prefer something somewhat formal but fun as well.
I'm open on whether the background is plain or has design in it. I don't have company logos.
Target Market(s)
Auto dealers, realtors and property managers
Industry/Entity Type
Business
Contact Information for Business Card
HOLLISTER FAMILY PROPERTIES, LLC
HOLLISTER PUBLISHING, LLC
LOTMASTER CONSULTING, LLC
Ned Hollister
2847 W. Tamarack Ave. #310
Boise, Idaho 83611-2905
208-514-3092
ned@holl5x.example

```html
<!DOCTYPE html>
<html lang="en">
<head>
<meta charset="utf-8">
<title>Ned Hollister – Business Card</title>
<link rel="stylesheet" href="https://fonts.googleapis.com/css2?family=Carlito:wght@400;700&display=swap">
<style>
  :root {
    --page-bg: #e9e8e6;
    --card-top: #ffffff;
    --card-bottom: #eeeeee;
    --accent-red: #e2455f;
    --accent-green: #74bf5e;
    --accent-blue: #6f73c2;
    --ink: #222222;
    --ink-soft: #555555;
    --mark-tone: #8a8fd0;
  }
  * { box-sizing: border-box; margin: 0; padding: 0; }
  html, body {
    width: 1200px;
    height: 600px;
    overflow: hidden;
    background: var(--page-bg);
    font-family: "Carlito", "Calibri", sans-serif;
  }
  .stage {
    width: 1200px;
    height: 600px;
    display: flex;
    align-items: center;
    justify-content: center;
  }
  .business-card {
    position: relative;
    width: 840px;
    height: 480px;
    border-radius: 30px;
    background: linear-gradient(160deg, var(--card-top) 0%, var(--card-top) 45%, var(--card-bottom) 100%);
    box-shadow: 0 6px 18px rgba(0, 0, 0, 0.12);
  }

  /* Left: company block */
  .company-block {
    position: absolute;
    left: 40px;
    top: 0;
    width: 380px;
    height: 100%;
    display: flex;
    flex-direction: column;
    align-items: center;
    justify-content: center;
  }
  .ornament-area {
    width: 150px;
    height: 62px;
    border-radius: 8px;
    background: linear-gradient(180deg, #a4a8de 0%, var(--mark-tone) 100%);
    opacity: 0.55;
    margin-bottom: 26px;
  }
  .company-list { list-style: none; text-align: center; }
  .company-name {
    font-size: 19px;
    letter-spacing: 0.5px;
    text-transform: uppercase;
    line-height: 1.55;
  }
  .company-name--properties { color: var(--accent-red); }
  .company-name--publishing { color: var(--accent-green); }
  .company-name--consulting { color: var(--accent-blue); }

  /* Divider */
  .divider {
    position: absolute;
    left: 440px;
    top: 70px;
    width: 2px;
    height: 340px;
    background: linear-gradient(180deg, var(--accent-red) 0%, var(--accent-blue) 100%);
    opacity: 0.7;
  }

  /* Right: contact block */
  .contact-block {
    position: absolute;
    left: 470px;
    top: 72px;
    width: 340px;
  }
  .person-name {
    font-size: 34px;
    font-weight: 700;
    color: var(--accent-red);
    line-height: 1.1;
  }
  .person-title {
    font-size: 22px;
    color: var(--ink-soft);
    margin-top: 4px;
    margin-bottom: 16px;
  }
  .contact-list { list-style: none; }
  .contact-item {
    display: flex;
    align-items: center;
    gap: 12px;
    font-size: 23px;
    color: var(--ink);
    line-height: 1.5;
  }
  .contact-icon {
    width: 18px;
    height: 18px;
    flex: none;
  }
  .mailing-address {
    font-style: normal;
    font-size: 25px;
    color: var(--ink);
    line-height: 1.25;
    margin-top: 22px;
  }
</style>
</head>
<body>
<main class="stage">
  <article class="business-card">
    <section class="company-block">
      <div class="ornament-area" role="img" aria-label="Decorative flourish ornament in soft blue-violet"></div>
      <ul class="company-list">
        <li class="company-name company-name--properties">Hollister Family Properties, LLC</li>
        <li class="company-name company-name--publishing">Hollister Publishing, LLC</li>
        <li class="company-name company-name--consulting">Lotmaster Consulting, LLC</li>
      </ul>
    </section>

    <div class="divider"></div>

    <section class="contact-block">
      <h1 class="person-name">Ned Hollister</h1>
      <p class="person-title">Owner</p>
      <ul class="contact-list">
        <li class="contact-item">
          <svg class="contact-icon" viewBox="0 0 18 18" aria-hidden="true">
            <rect width="18" height="18" rx="3" fill="#e2455f"/>
            <path d="M5 4.5c.6-.6 1.4-.6 1.8 0l1 1.4c.3.4.2 1-.2 1.3l-.6.5c.5 1.2 1.4 2.1 2.6 2.6l.5-.6c.3-.4.9-.5 1.3-.2l1.4 1c.6.4.6 1.2 0 1.8l-.6.6c-.8.8-2.2.8-4.2-.8C5.9 10.5 4.6 8.8 4.4 7.1c-.1-.9.1-1.6.6-2.1z" fill="#fff"/>
          </svg>
          <span>208-514-3092</span>
        </li>
        <li class="contact-item">
          <svg class="contact-icon" viewBox="0 0 18 18" aria-hidden="true">
            <rect width="18" height="18" rx="3" fill="#e2455f"/>
            <rect x="3.5" y="5" width="11" height="8" rx="1" fill="#fff"/>
            <path d="M3.8 5.4 9 9.6l5.2-4.2" fill="none" stroke="#e2455f" stroke-width="1.2"/>
          </svg>
          <span>ned@holl5x.example</span>
        </li>
        <li class="contact-item">
          <svg class="contact-icon" viewBox="0 0 18 18" aria-hidden="true">
            <circle cx="9" cy="9" r="9" fill="#e2455f"/>
            <circle cx="9" cy="9" r="5.5" fill="none" stroke="#fff" stroke-width="1.2"/>
            <ellipse cx="9" cy="9" rx="2.4" ry="5.5" fill="none" stroke="#fff" stroke-width="1.1"/>
            <path d="M3.5 9h11" stroke="#fff" stroke-width="1.1"/>
          </svg>
          <span>www.holl5x.example</span>
        </li>
      </ul>
      <address class="mailing-address">
        2847 W. Tamarack Ave.<br>
        #310 Boise,<br>
        Idaho 83611-2905
      </address>
    </section>
  </article>
</main>
</body>
</html>
```